Harbinger Postcard Design

We need postcard designs for a new company based in Maryland called "Harbinger". We provide security guard services and we provide training for security guards. We would like two different cards, one for individuals who need training to become security guards through our training academy, and one targeted at businesses that are looking to hire security guards through our security agency. We are looking to project an image of strength, stability, trustworthiness and confidence.

Target Market(s)

Businesses that typically use security guard services, such as property management companies, restaurants, construction companies, etc.

Industry/Entity Type

Security

Requirements
Must have
• The card should be professional. It needs to grab the reader's attention right away.

```html
<!DOCTYPE html>
<html lang="en">
<head>
<meta charset="utf-8">
<title>Harbinger Security Postcard</title>
<link rel="stylesheet" href="https://fonts.googleapis.com/css2?family=Bebas+Neue&family=Oswald:wght@500;600&family=Arimo:wght@400&display=swap">
<style>
  :root {
    --page: #ffffff;
    --panel-light: #1d6c8c;
    --panel-mid: #124a68;
    --panel-dark: #082a43;
    --sky-top: #8fb8dc;
    --sky-low: #dfe9f2;
    --tower: #6d8aa8;
    --ink-light: #ffffff;
    --check: #2fa8d8;
    --ink-dark: #222222;
    --rule: #d9d9d9;
    --stamp: #d6d6d6;
  }
  * { margin: 0; padding: 0; box-sizing: border-box; }
  html, body { width: 1200px; height: 930px; overflow: hidden; background: var(--page); }
  .postcard { position: relative; width: 1200px; height: 930px; background: var(--page); }

  .front { position: absolute; left: 0; top: 0; width: 580px; height: 760px; }
  .hero {
    position: absolute; left: 0; top: 0; width: 580px; height: 311px;
    background: linear-gradient(180deg, var(--sky-top) 0%, var(--sky-low) 55%, var(--tower) 100%);
  }
  .services {
    position: absolute; left: 0; top: 311px; width: 580px; height: 449px;
    background: radial-gradient(ellipse at 45% 20%, var(--panel-light) 0%, var(--panel-mid) 45%, var(--panel-dark) 100%);
  }
  .services-title {
    position: absolute; left: 46px; top: 24px;
    font-family: "Bebas Neue", sans-serif; font-size: 50px; line-height: 1;
    color: var(--ink-light); letter-spacing: 0.5px;
  }
  .service-list { position: absolute; left: 50px; top: 84px; list-style: none; }
  .service-list li {
    position: relative; padding-left: 30px; margin-bottom: 11px;
    font-family: "Oswald", sans-serif; font-weight: 500; font-size: 21px; line-height: 23px;
    color: var(--ink-light); text-transform: uppercase; letter-spacing: 0.3px;
  }
  .service-list li svg { position: absolute; left: 0; top: 2px; width: 20px; height: 20px; }
  .brand { position: absolute; left: 364px; top: 362px; display: flex; align-items: center; gap: 10px; }
  .brand-dot { width: 60px; height: 60px; border-radius: 50%; background: var(--ink-light); opacity: 0.85; }
  .brand-name {
    font-family: "Oswald", sans-serif; font-weight: 600; font-size: 28px; line-height: 29px;
    color: var(--ink-light); text-transform: uppercase;
  }

  .mailing { position: absolute; left: 580px; top: 0; width: 620px; height: 760px; }
  .return-address {
    position: absolute; left: 0; top: 114px; width: 330px; text-align: center;
    font-family: "Arimo", sans-serif; font-size: 19px; line-height: 23px; color: var(--ink-dark);
    letter-spacing: -0.4px;
  }
  .return-address .phone { margin-top: 14px; }
  .stamp-box {
    position: absolute; left: 327px; top: 35px; width: 265px; height: 265px;
    border: 3px solid var(--stamp);
  }
  .address-line {
    position: absolute; left: 52px; width: 495px; height: 3px; background: var(--rule);
  }
</style>
</head>
<body>
<main class="postcard">
  <section class="front">
    <div class="hero" role="img" aria-label="Photo of a uniformed security guard from behind, facing downtown glass skyscrapers"></div>
    <div class="services">
      <h2 class="services-title">We Provide:</h2>
      <ul class="service-list">
        <li><svg viewBox="0 0 20 20"><circle cx="10" cy="10" r="10" fill="var(--check)"/><path d="M5.5 10.2l3 3 6-6.2" fill="none" stroke="#fff" stroke-width="2.4" stroke-linecap="round" stroke-linejoin="round"/></svg>Armed and unarmed uninformed<br>security guards</li>
        <li><svg viewBox="0 0 20 20"><circle cx="10" cy="10" r="10" fill="var(--check)"/><path d="M5.5 10.2l3 3 6-6.2" fill="none" stroke="#fff" stroke-width="2.4" stroke-linecap="round" stroke-linejoin="round"/></svg>Private detective</li>
        <li><svg viewBox="0 0 20 20"><circle cx="10" cy="10" r="10" fill="var(--check)"/><path d="M5.5 10.2l3 3 6-6.2" fill="none" stroke="#fff" stroke-width="2.4" stroke-linecap="round" stroke-linejoin="round"/></svg>Personal protection</li>
        <li><svg viewBox="0 0 20 20"><circle cx="10" cy="10" r="10" fill="var(--check)"/><path d="M5.5 10.2l3 3 6-6.2" fill="none" stroke="#fff" stroke-width="2.4" stroke-linecap="round" stroke-linejoin="round"/></svg>Background checks</li>
        <li><svg viewBox="0 0 20 20"><circle cx="10" cy="10" r="10" fill="var(--check)"/><path d="M5.5 10.2l3 3 6-6.2" fill="none" stroke="#fff" stroke-width="2.4" stroke-linecap="round" stroke-linejoin="round"/></svg>Marked vehicle patrols</li>
        <li><svg viewBox="0 0 20 20"><circle cx="10" cy="10" r="10" fill="var(--check)"/><path d="M5.5 10.2l3 3 6-6.2" fill="none" stroke="#fff" stroke-width="2.4" stroke-linecap="round" stroke-linejoin="round"/></svg>Security consulting and risk assessment</li>
      </ul>
      <div class="brand">
        <span class="brand-dot"></span>
        <span class="brand-name">Harbinger<br>Security</span>
      </div>
    </div>
  </section>

  <section class="mailing">
    <address class="return-address" style="font-style:normal">
      <p>2240 Meridian Avenue, Suite 310,<br>Glenwood Heights, MD 20916</p>
      <p class="phone">301-555-0148</p>
    </address>
    <div class="stamp-box"></div>
    <div class="address-line" style="top:420px"></div>
    <div class="address-line" style="top:504px"></div>
    <div class="address-line" style="top:586px"></div>
    <div class="address-line" style="top:668px"></div>
  </section>
</main>
</body>
</html>
```